Web design for Software Innovators of the Medical Marijuana Industry

We are a software company that provides web-based medical marijuana solutions for the entire seed-to-sale process and dispenser/pos. We are looking to update the design of our website. http://www.stemvaro.com/
Terms:
Seed to Sale - Tracking the progress of the growing of the plants.
Dispenser / POS - ORDERING & SALES
Here are our competitors
www.quibrel.com
www.tnparkline.com
www.orvasynqed.com
Design Must include
- Menu : Home, About Us, Products, News, Contact
- our logo
- a button for login which takes clients to login page
-a button which says "more info" .. .which opens a new page that will tells them about
- Area for uncoming dates/events such as
4th Annual Cannabis Trade Summit & Showcase
Nov 11-13 @ Stem Varo booth number 727
- Area for blog/news posts (list maybe 2-3 blog posts)
- an area to write a intro/welcome text
- an area to features "Seed to Sale" and "Dispenser / POS"
We are looking for a feel that is
- clean
- peaceful
- professional
I am looking for Homepage Design and Inner Page design

```html
<!DOCTYPE html>
<html lang="en">
<head>
<meta charset="utf-8">
<title>Stem Varo Technology</title>
<link href="https://fonts.googleapis.com/css2?family=Open+Sans:wght@400;600;700;800&display=swap" rel="stylesheet">
<style>
:root{
  --green:#56a35c;
  --green-dark:#3f8a47;
  --green-deep:#2f6d37;
  --ink:#2f3535;
  --charcoal:#3b4041;
  --charcoal-2:#323637;
  --paper:#f1f2f1;
  --card:#ffffff;
  --muted:#6d7473;
  --line:#d9dcda;
}
*{box-sizing:border-box;margin:0;padding:0}
html,body{width:710px;height:1200px;overflow:hidden}
body{font-family:"Open Sans",Arial,sans-serif;color:var(--ink);background:#fff;font-size:9px}
.page{width:710px;height:1200px;position:relative;overflow:hidden}

/* header */
.site-header{position:absolute;top:0;left:0;width:710px;height:33px;background:rgba(40,46,44,.88);display:flex;align-items:center;justify-content:space-between;padding:0 18px 0 22px;z-index:2}
.brand{display:flex;align-items:center;gap:6px;background:#fff;height:22px;padding:0 10px 0 6px;border-radius:2px}
.brand-dot{width:10px;height:10px;background:var(--green);border-radius:50%}
.brand-name{font-weight:700;font-size:10px;color:var(--green-dark)}
.main-nav{display:flex;align-items:center;gap:22px}
.main-nav a{color:#fff;text-decoration:none;font-size:7.5px;font-weight:600;letter-spacing:.5px}
.main-nav .login{background:var(--green);padding:5px 10px;border-radius:2px}

/* hero */
.hero{position:absolute;top:0;left:0;width:710px;height:256px;background:linear-gradient(180deg,#8fae8a 0%,#5e8a5d 40%,#3f5f45 75%,#4c5a52 100%)}
.hero-copy{position:absolute;left:0;right:0;top:140px;text-align:center;color:#fff}
.hero-title{font-size:25px;font-weight:800;letter-spacing:1px}
.hero-sub{font-size:10px;margin-top:6px;color:#dfeadb}
.hero-sub strong{color:#fff;font-weight:700}
.btn-outline{display:inline-block;border:1px solid #fff;color:#fff;font-size:7.5px;padding:5px 12px;border-radius:2px;margin-top:16px;text-decoration:none}

/* welcome */
.welcome{position:absolute;top:256px;left:0;width:710px;height:292px;background:var(--paper);text-align:center}
.welcome h1{font-size:20px;font-weight:700;margin-top:36px;color:var(--ink)}
.welcome h1 span{color:var(--green-dark)}
.welcome-lead{font-size:7.5px;color:var(--muted);margin-top:8px}
.divider{display:flex;align-items:center;justify-content:center;gap:6px;margin-top:10px}
.divider i{display:block;width:70px;height:1px;background:var(--line)}
.divider b{width:6px;height:6px;border-radius:50%;background:var(--green)}
.cards{display:flex;justify-content:center;gap:27px;margin-top:22px}
.card{width:130px;height:150px;background:var(--card);box-shadow:0 1px 3px rgba(0,0,0,.12);position:relative;padding-top:30px}
.card-icon{position:absolute;top:-16px;left:50%;margin-left:-18px;width:36px;height:36px;border-radius:50%;background:var(--green);border:3px solid #fff;display:flex;align-items:center;justify-content:center}
.card h3{font-size:9px;font-weight:700;background:#e9ecea;padding:6px 0;margin:0 0 8px}
.card p{font-size:6.5px;line-height:1.55;color:var(--muted);padding:0 10px;text-align:left}
.card p strong{color:var(--ink)}
.card-more{position:absolute;bottom:10px;left:50%;margin-left:-7px;width:14px;height:14px;border-radius:50%;background:var(--green)}

/* product */
.product{position:absolute;top:548px;left:0;width:710px;height:224px;background:linear-gradient(90deg,var(--green-dark),var(--green))}
.product-copy{position:absolute;left:80px;top:26px;width:270px;color:#fff}
.product-copy h2{font-size:17px;font-weight:700;display:flex;align-items:center;gap:6px}
.product-copy p{font-size:7.5px;line-height:1.6;margin-top:12px;color:#e6f1e4}
.product-copy .btn-outline{margin-top:40px}
.product-visual{position:absolute;left:360px;top:-14px;width:320px;height:238px;background:linear-gradient(160deg,#7b8a80,#3e4a44);border-radius:4px}

/* features */
.features{position:absolute;top:772px;left:0;width:710px;height:168px;background:#fff;display:flex;justify-content:center;gap:14px;padding-top:14px}
.feature{width:130px}
.feature-head{display:flex;align-items:center;gap:6px;border-bottom:1px solid var(--line);padding-bottom:6px}
.feature-icon{width:24px;height:24px;background:var(--charcoal);border-radius:2px;flex:none}
.feature-head h4{font-size:9px;font-weight:800;line-height:1.05;white-space:nowrap}
.feature-head h4 small{display:block;font-size:6px;font-weight:400;color:var(--muted)}
.feature ul{list-style:none;margin-top:6px}
.feature li{font-size:6.5px;color:var(--ink);padding:3.5px 0;display:flex;align-items:center;gap:5px;white-space:nowrap}
.feature li::before{content:"";width:4px;height:4px;background:var(--green);border-radius:50%;flex:none}

/* footer */
.site-footer{position:absolute;top:940px;left:0;width:710px;height:260px;display:flex}
.news{width:258px;background:var(--green-dark);color:#fff;padding:18px 20px}
.news h5,.newsletter h5,.find-us h5{font-size:10px;font-weight:700;letter-spacing:.5px;margin-bottom:14px}
.news-item{display:flex;gap:8px;margin-bottom:14px}
.news-thumb{width:36px;height:30px;background:linear-gradient(135deg,#8fbf88,#4d7a52);flex:none}
.news-item p{font-size:6.5px;line-height:1.45;color:#e1eedf}
.news-item p strong{color:#fff;display:block}
.newsletter{width:242px;background:var(--charcoal);color:#dfe3e1;padding:18px 18px}
.newsletter p{font-size:7px;line-height:1.5;margin-bottom:10px}
.subscribe{display:flex}
.subscribe span{flex:1;height:20px;background:#fff}
.subscribe b{background:#fff;color:var(--ink);font-size:7px;font-weight:600;padding:0 10px;display:flex;align-items:center;border-left:1px solid var(--line)}
.follow{display:flex;align-items:center;gap:6px;margin-top:60px;font-size:9px;font-weight:600;color:#fff}
.follow i{width:14px;height:14px;border-radius:50%;background:#fff;display:block}
.find-us{flex:1;background:var(--charcoal-2);color:#d6dbd9;padding:18px 18px}
.find-row{display:flex;gap:7px;font-size:7px;line-height:1.5;margin-bottom:8px;align-items:flex-start}
.find-row svg{flex:none;margin-top:1px}
.copyright{font-size:6px;color:#9aa19e;margin-top:70px;line-height:1.5}
</style>
</head>
<body>
<div class="page">

  <section class="hero" role="img" aria-label="Young plant seedlings growing in rows under soft light">
    <div class="hero-copy">
      <div class="hero-title">STEM VARO TECHNOLOGY</div>
      <div class="hero-sub">Software Innovators Of The Medical <strong>MARIJUANA INDUSTRY</strong></div>
      <a class="btn-outline" href="#">Learn More</a>
    </div>
  </section>

  <header class="site-header">
    <div class="brand"><span class="brand-dot"></span><span class="brand-name">Stem Varo Technology</span></div>
    <nav class="main-nav">
      <a href="#">HOME</a><a href="#">ABOUT US</a><a href="#">SERVICES</a><a href="#">FAQ</a><a href="#">CONTACT</a><a class="login" href="#">LOGIN</a>
    </nav>
  </header>

  <section class="welcome">
    <h1>Welcome to <span>Stemvaro</span></h1>
    <p class="welcome-lead">Stem Varo Technology is a software company providing solutions for the Medical Marijuana Industry.</p>
    <div class="divider"><i></i><b></b><i></i></div>
    <div class="cards">
      <article class="card">
        <div class="card-icon"><svg width="14" height="14" viewBox="0 0 14 14"><circle cx="7" cy="7" r="6" fill="none" stroke="#fff" stroke-width="1.5"/><rect x="6.2" y="6" width="1.6" height="4.5" fill="#fff"/><circle cx="7" cy="4" r="1" fill="#fff"/></svg></div>
        <h3>ABOUT US</h3>
        <p><strong>StemVaro Technology</strong> We offer web-based medical marijuana solutions for the entire seed-to-sale process. Our core products [...]</p>
        <span class="card-more"></span>
      </article>
      <article class="card">
        <div class="card-icon"><svg width="14" height="14" viewBox="0 0 14 14"><circle cx="7" cy="7" r="4" fill="none" stroke="#fff" stroke-width="2"/><circle cx="7" cy="7" r="1.4" fill="#fff"/></svg></div>
        <h3>HOW IT WORKS?</h3>
        <p><strong>Integrated Solutions</strong> From seed to sale, every plant is tracked and every order flows into a single dispensary system [...]</p>
        <span class="card-more"></span>
      </article>
      <article class="card">
        <div class="card-icon"><svg width="14" height="14" viewBox="0 0 14 14"><path d="M3 7.5l2.5 2.5L11 4" fill="none" stroke="#fff" stroke-width="2"/></svg></div>
        <h3>WHAT WE DO?</h3>
        <p><strong>Differentiate</strong> - You lead the competition through our comprehensive medical marijuana software [...]</p>
        <span class="card-more"></span>
      </article>
    </div>
  </section>

  <section class="product">
    <div class="product-copy">
      <h2><svg width="10" height="12" viewBox="0 0 10 12"><path d="M1 1l8 5-8 5z" fill="#fff"/></svg>Product Introduction!</h2>
      <p>Our platform follows each plant from the first seed to the final sale. Growers, dispensaries and patients share one clean system for tracking, ordering, compliance and reporting, built to keep daily work calm and simple.</p>
      <a class="btn-outline" href="#">Learn More</a>
    </div>
    <div class="product-visual" role="img" aria-label="Hands holding a tablet showing the software dashboard"></div>
  </section>

  <section class="features">
    <div class="feature">
      <div class="feature-head"><span class="feature-icon"></span><h4>SOFTWARE<small>Products</small></h4></div>
      <ul><li>Stem - Grower</li><li>Stem - Dispensary</li><li>Stem - Patient</li><li>Stem - With Financial</li><li>Stem - Visibility</li></ul>
    </div>
    <div class="feature">
      <div class="feature-head"><span class="feature-icon"></span><h4>Technology<small>Included</small></h4></div>
      <ul><li>Stem "Cloud" Solutions</li><li>Stem "Web" Solution</li><li>Stem "Desktop" Solution</li><li>Stem "Mobile" Solutions</li><li>Stem Technology</li></ul>
    </div>
    <div class="feature">
      <div class="feature-head"><span class="feature-icon"></span><h4>Software<small>Efficiency</small></h4></div>
      <ul><li>Stem Collaboration</li><li>Stem Workflow</li><li>Stem Performance</li><li>Stem Data</li></ul>
    </div>
    <div class="feature">
      <div class="feature-head"><span class="feature-icon"></span><h4>Cost Saving &amp;<small>ROI Services</small></h4></div>
      <ul><li>Stem Hosted Solution</li><li>Customer Hosted Solution</li><li>Pay-per Transaction Pricing</li><li>Customizable Solution</li></ul>
    </div>
  </section>

  <footer class="site-footer">
    <div class="news">
      <h5>Latest News</h5>
      <div class="news-item"><span class="news-thumb" role="img" aria-label="News photo"></span><p><strong>New grower module released</strong>Seed tracking now runs faster on every device in your facility.</p></div>
      <div class="news-item"><span class="news-thumb" role="img" aria-label="News photo"></span><p><strong>Meet us at the summit</strong>Nov 11-13, Stem Varo booth number 727, Cannabis Trade Summit.</p></div>
      <div class="news-item"><span class="news-thumb" role="img" aria-label="News photo"></span><p><strong>Dispensary POS update</strong>Ordering and sales reports now export in a single simple click.</p></div>
    </div>
    <div class="newsletter">
      <h5>NEWSLETTER SIGNUP</h5>
      <p>Get the latest updates by<br>entering your email address</p>
      <div class="subscribe"><span></span><b>Subscribe</b></div>
      <div class="follow">Follow Us <i></i><i></i><i></i><i></i></div>
    </div>
    <div class="find-us">
      <h5>FIND US</h5>
      <div class="find-row"><svg width="8" height="10" viewBox="0 0 8 10"><path d="M4 0a3.5 3.5 0 0 0-3.5 3.5C.5 6 4 10 4 10s3.5-4 3.5-6.5A3.5 3.5 0 0 0 4 0z" fill="#56a35c"/><circle cx="4" cy="3.5" r="1.2" fill="#323637"/></svg><span>250 Larkmoor Ave<br>Suite 14<br>Fenwick, Georgia 30107</span></div>
      <div class="find-row"><svg width="8" height="10" viewBox="0 0 8 10"><path d="M1.5 0h2l.5 2.5-1.3.8a5 5 0 0 0 2 3l.8-1.3L8 5.5v2C8 9 6.5 10 5 9.5 2.5 8.5.5 6 0 3.5-.3 1.5.5 0 1.5 0z" fill="#56a35c"/></svg><span>+1 (404) 555-0186</span></div>
      <div class="find-row"><svg width="9" height="7" viewBox="0 0 9 7"><rect width="9" height="7" fill="#56a35c"/><path d="M0 0l4.5 4L9 0" fill="none" stroke="#323637"/></svg><span>info@stemvaro.com</span></div>
      <p class="copyright">© 2015 Stem Varo Technologies<br>All Rights Reserved.</p>
    </div>
  </footer>

</div>
</body>
</html>
```